Scrap Metal Recycling

We are looking for a simple yet bold business card. We already have the logo, please see attached. Color scheme of blue, black and white or just blue and white.

```html
<!DOCTYPE html>
<html lang="en">
<head>
<meta charset="utf-8">
<title>Northbank Metals Inc. – Business Card</title>
<link rel="stylesheet" href="https://fonts.googleapis.com/css2?family=Arimo:wght@400;700&family=Open+Sans:wght@600&display=swap">
<style>
  :root {
    --page-bg: #2a2627;
    --card-bg: #3a3a3b;
    --brand-blue: #168db5;
    --text-white: #ffffff;
    --text-soft: #e9e9e9;
  }
  * { box-sizing: border-box; margin: 0; padding: 0; }
  html, body {
    width: 1200px; height: 912px; overflow: hidden;
    background: var(--page-bg);
    font-family: "Arimo", Arial, sans-serif;
  }
  .sheet {
    width: 1200px; height: 912px;
    display: flex; flex-direction: column; align-items: center; justify-content: center;
    gap: 44px;
  }
  .card {
    position: relative;
    width: 680px; height: 389px;
    background: var(--card-bg);
    border-radius: 18px;
    box-shadow: 0 10px 24px rgba(0,0,0,.45);
    overflow: hidden;
  }
  .brand-name {
    font-family: "Arimo", Arial, sans-serif;
    font-weight: 700;
    color: var(--text-white);
    letter-spacing: .5px;
    white-space: nowrap;
  }
  .brand-tagline {
    font-family: "Open Sans", Arial, sans-serif;
    font-weight: 600;
    color: var(--brand-blue);
    text-transform: uppercase;
    white-space: nowrap;
  }
  /* front */
  .card-front .brand {
    position: absolute; inset: 0;
    display: flex; flex-direction: column; align-items: center; justify-content: center;
    gap: 10px;
  }
  .card-front .brand-name { font-size: 44px; }
  .card-front .brand-tagline { font-size: 22px; letter-spacing: 9px; }
  /* back */
  .card-back .brand {
    position: absolute; left: 48px; top: 48px;
  }
  .card-back .brand-name { font-size: 30px; }
  .card-back .brand-tagline { font-size: 15px; letter-spacing: 6px; margin-top: 6px; }
  .person {
    position: absolute; left: 78px; top: 170px;
  }
  .person-accent {
    position: absolute; left: 48px; top: 176px;
    width: 12px; height: 44px; background: var(--brand-blue);
  }
  .person-name {
    font-weight: 700; font-size: 28px; color: var(--text-white);
    text-transform: uppercase; letter-spacing: .3px;
  }
  .person-title {
    font-size: 20px; color: var(--brand-blue); margin-top: 4px;
  }
  .contact-list {
    position: absolute; left: 78px; top: 258px;
    list-style: none;
    display: flex; flex-direction: column; gap: 8px;
  }
  .contact-item {
    display: flex; align-items: center; gap: 10px;
    font-size: 18px; color: var(--text-soft);
  }
  .contact-icon { width: 16px; height: 16px; flex: none; }
</style>
</head>
<body>
<main class="sheet">
  <section class="card card-front" aria-label="Card front">
    <div class="brand">
      <div class="brand-name">NORTHBANK METALS INC.</div>
      <div class="brand-tagline">Scrap Metal Recycling</div>
    </div>
  </section>

  <section class="card card-back" aria-label="Card back">
    <div class="brand">
      <div class="brand-name">NORTHBANK METALS INC.</div>
      <div class="brand-tagline">Scrap Metal Recycling</div>
    </div>

    <span class="person-accent"></span>
    <div class="person">
      <div class="person-name">Daniel Whitford</div>
      <div class="person-title">Founder &amp; CEO</div>
    </div>

    <ul class="contact-list">
      <li class="contact-item">
        <svg class="contact-icon" viewBox="0 0 16 16"><path fill="#168db5" d="M3.5 1.5l2.5 3-1.5 1.8c.8 1.8 2.2 3.2 4 4l1.8-1.5 3 2.5-1.6 2.2C6.5 13.2 2.8 9.5 1.3 3.1z"/></svg>
        555-014-2290
      </li>
      <li class="contact-item">
        <svg class="contact-icon" viewBox="0 0 16 16"><rect x="4" y="1" width="8" height="14" rx="1.5" fill="none" stroke="#168db5" stroke-width="1.6"/><circle cx="8" cy="12.5" r="0.9" fill="#168db5"/></svg>
        555-014-2290
      </li>
      <li class="contact-item">
        <svg class="contact-icon" viewBox="0 0 16 16"><rect x="1" y="3" width="14" height="10" rx="1" fill="#168db5"/><path d="M1.5 3.8L8 9l6.5-5.2" fill="none" stroke="#3a3a3b" stroke-width="1.3"/></svg>
        info@northbankmetals.com
      </li>
      <li class="contact-item">
        <svg class="contact-icon" viewBox="0 0 16 16"><circle cx="8" cy="8" r="7" fill="#168db5"/><path d="M1 8h14M8 1c-2.5 2.5-2.5 11.5 0 14M8 1c2.5 2.5 2.5 11.5 0 14" fill="none" stroke="#3a3a3b" stroke-width="1"/></svg>
        www.northbankmetals.com
      </li>
    </ul>
  </section>
</main>
</body>
</html>
```